Need innovative card design for tech start up

We are a Santa Monica based marketing analytics software start up called Brightmere Tally. We're launching a platform that will help advertisers better measure and optimize their marketing spend by using advanced algorithmic analytic. While our subject matter is complicated, we want to convey simple, clean, curated. We also want to stand out - ad tech is a sea of sameness and we need to have some individuality. We have an established color palette and would like to see a design we could print in each tone (teal, tangerine, grey), but it doesn't require the card to be monochromatic. The font used is DENSE.

```html
<!DOCTYPE html>
<html lang="en">
<head>
<meta charset="utf-8">
<title>Brightmere Tally – Business Card</title>
<link href="https://fonts.googleapis.com/css2?family=League+Spartan:wght@400;600&display=swap" rel="stylesheet">
<style>
  :root {
    --tangerine: #ff9d00;
    --paper: #ffffff;
    --ink: #1f1f1f;
    --grey-text: #3a3a3a;
    --stage: #ececea;
    --shadow: rgba(0, 0, 0, 0.18);
  }
  * { box-sizing: border-box; margin: 0; padding: 0; }
  html, body {
    width: 1200px;
    height: 1000px;
    overflow: hidden;
    background: var(--stage);
    font-family: "League Spartan", "Century Gothic", sans-serif;
  }
  .canvas {
    position: relative;
    width: 1200px;
    height: 1000px;
  }
  .card {
    position: absolute;
    width: 540px;
    height: 308px;
    box-shadow: 0 4px 14px var(--shadow);
  }
  .card--front {
    left: 210px;
    top: 165px;
    background: var(--tangerine);
    display: flex;
    align-items: center;
    justify-content: center;
  }
  .front-wordmark {
    color: var(--paper);
    font-size: 42px;
    font-weight: 400;
    letter-spacing: 0.04em;
    text-transform: uppercase;
  }
  .card--back {
    left: 440px;
    top: 505px;
    background: var(--paper);
  }
  .brand-block {
    position: absolute;
    left: 48px;
    top: 36px;
    width: 170px;
  }
  .brand-square {
    display: block;
    width: 170px;
    height: 170px;
    background: var(--tangerine);
  }
  .brand-name {
    margin-top: 8px;
    color: var(--tangerine);
    font-size: 19px;
    font-weight: 400;
    letter-spacing: 0.02em;
    text-transform: uppercase;
    white-space: nowrap;
  }
  .contact {
    position: absolute;
    left: 262px;
    top: 40px;
    color: var(--grey-text);
    font-size: 17px;
    line-height: 1.2;
    white-space: nowrap;
  }
  .contact__name {
    color: var(--tangerine);
    font-weight: 600;
    font-size: 16.5px;
  }
  .contact__title {
    color: var(--tangerine);
    font-size: 17px;
    margin-bottom: 20px;
  }
  .contact__address { margin-bottom: 18px; }
  .contact__web {
    color: var(--ink);
    font-weight: 600;
    font-size: 16.5px;
  }
</style>
</head>
<body>
  <main class="canvas">
    <section class="card card--front" aria-label="Card front">
      <span class="front-wordmark">Brightmere Tally</span>
    </section>

    <section class="card card--back" aria-label="Card back">
      <div class="brand-block">
        <span class="brand-square" aria-hidden="true"></span>
        <p class="brand-name">Brightmere Tally</p>
      </div>
      <div class="contact">
        <p class="contact__name">Dorian Kessel</p>
        <p class="contact__title">Founder/CEO</p>
        <p class="contact__address">
          1480 Harbor Crest, suite 310<br>
          Westhaven, CA 90417<br>
          office: 310-555-0148 x101<br>
          mobile: 310-555-0192
        </p>
        <p class="contact__web">
          dorian@brightmeretally.com<br>
          www.brightmeretally.com
        </p>
      </div>
    </section>
  </main>
</body>
</html>
```